Brochure / Leaflet Required

Hi!
We need a cool brochure / leaflet for our Plexon product line.
These are plastic corrugated sheets which are used to make various products.
When you look at the Plexon section on our website: http://velmarto.example/plexon/ you will get a bit more info (the website is under construction).
We need a separate page for a few products.
But for now we need just one test page for the first product group "Surface Protection". If your design is approved as a template, we will give you the text and pics for the other products. We can set a price per page for the other pages later.
Requirements:
- Size should be A4. The leaflet will be combined into one full brochure at the end. But each page will also need to function a a separate leaflet for that particular product. (For example it will also be placed on the website as a downloadable PDF)
- Font needs to be Gill Sans MT
- This is the brand logo: https://files.quorvik.example/s/k2b81tdex9ma3q1/Plexon%20logo%20-%20registered.ai?dl=0
- These 3 pics should be use on leaflet: https://files.quorvik.example/sh/71xq4mbn2vk8r0w/BBDm8upSwgoMvYZ3LLx5rRhWb?dl=0
- Here you can find the text: https://files.quorvik.example/s/p9h27wlcrzt45ej/Text%20-%20Surface%20Protection.docx?dl=0
- The icons in this text part (including text) also need to be placed in the brochure. The originals can be found here: https://files.quorvik.example/sh/83jm51640hgo2tz/BBEqtZZZ3xxt3NbAxaznv6nLb?dl=0
Please think outside of the box as much as possible.
And make sure to use mainly white and the "Plexon logo" blue.
We also have another product group which will need to be done after this project.
Looking forward to your design!
Regards,
Teun
Target Market(s)
Construction
Industry/Entity Type
Plastic
Look and feel

```html
<!DOCTYPE html>
<html lang="en">
<head>
<meta charset="utf-8">
<title>Plexon Specifications</title>
<link href="https://fonts.googleapis.com/css2?family=Cabin:wght@400;500;700&display=swap" rel="stylesheet">
<style>
:root{
  --brand:#2a72b9;
  --brand-dark:#1f5c99;
  --ink:#231f20;
  --paper:#ffffff;
  --rule:#9dc0e4;
}
*{margin:0;padding:0;box-sizing:border-box}
html,body{width:848px;height:1200px;overflow:hidden;background:var(--paper)}
body{font-family:"Cabin",sans-serif;color:var(--ink);position:relative}
.band{position:absolute;left:0;width:848px;background:var(--brand);color:#fff;font-weight:700;display:flex;align-items:center;padding-left:40px}
.band--specs{top:0;height:66px;font-size:25px}
.band--features{top:742px;height:56px;font-size:25px}
.band--options{top:979px;height:48px;font-size:28px;letter-spacing:.3px}
.spec{position:absolute;left:0;width:848px}
.spec__icon{position:absolute;left:34px;top:-2px;width:40px;height:40px}
.spec__title{position:absolute;left:105px;top:0;font-size:20px;font-weight:700;color:var(--brand);white-space:nowrap}
.spec__text{position:absolute;left:180px;top:24px;width:580px;font-size:13.6px;line-height:18px}
.feature{position:absolute;transform:translateX(-50%);text-align:center;font-size:14.5px;white-space:nowrap}
.feature svg{display:block;margin:0 auto 6px;width:42px;height:42px}
.sep{position:absolute;width:3px;height:24px;background:var(--brand)}
.option{position:absolute;top:1040px}
.option__icon{position:absolute;top:24px;width:46px;height:46px}
.option__title{font-size:20px;font-weight:700;color:var(--brand);line-height:20px}
.option__text{font-size:13px;line-height:15px;text-align:justify;width:194px;margin-top:1px}
</style>
</head>
<body>

<header class="band band--specs">Plexon Specifications:</header>

<svg width="0" height="0" style="position:absolute">
  <defs>
    <symbol id="ring" viewBox="0 0 40 40"><circle cx="20" cy="20" r="18" fill="none" stroke="var(--brand)" stroke-width="2"/><circle cx="20" cy="20" r="14.5" fill="var(--brand)"/></symbol>
    <symbol id="disc" viewBox="0 0 42 42"><circle cx="21" cy="21" r="20" fill="var(--brand)"/><circle cx="21" cy="21" r="17" fill="none" stroke="#fff" stroke-width="1.2"/></symbol>
  </defs>
</svg>

<section class="specs">
  <div class="spec" style="top:92px">
    <svg class="spec__icon" viewBox="0 0 40 40"><use href="#ring"/><path d="M20 11v18M16 14h8M17 26h6" stroke="#fff" stroke-width="2" fill="none"/></svg>
    <h3 class="spec__title">Thickness</h3>
    <p class="spec__text">Plexon sheets can be produced in a thickness between 1.5 and 10 mm. We can advise you on what thickness to choose depending on the purpose of use.</p>
  </div>
  <div class="spec" style="top:152px">
    <svg class="spec__icon" viewBox="0 0 40 40"><use href="#ring"/><path d="M20 12v16M13 15h14M13 15l-3 7h6zM27 15l-3 7h6zM16 28h8" stroke="#fff" stroke-width="1.6" fill="none"/></svg>
    <h3 class="spec__title">Weight</h3>
    <p class="spec__text">The weight of Plexon sheets is expressed in GSM (grams per square meter). The higher you choose your GSM, the stronger and stiffer the material will be.</p>
  </div>
  <div class="spec" style="top:213px">
    <svg class="spec__icon" viewBox="0 0 40 40"><use href="#ring"/><rect x="12" y="14" width="16" height="12" fill="none" stroke="#fff" stroke-width="1.8"/><circle cx="20" cy="20" r="2.5" fill="#fff"/></svg>
    <h3 class="spec__title">Size</h3>
    <p class="spec__text">Plexon sheets are available in any requested size. The length can be as long as required; the width is limited to 240 cm.</p>
  </div>
  <div class="spec" style="top:273px">
    <svg class="spec__icon" viewBox="0 0 40 40"><use href="#ring"/><path d="M13 27l9-14M17 27l8-12M21 27l6-9" stroke="#fff" stroke-width="2" fill="none"/></svg>
    <h3 class="spec__title">Color</h3>
    <p class="spec__text">Our customers can choose any color for the sheets or artwork. Just ask us what you need, and we can provide you with a sample.</p>
  </div>
  <div class="spec" style="top:333px">
    <svg class="spec__icon" viewBox="0 0 40 40"><use href="#ring"/><path d="M20 12l8 14H12z" fill="none" stroke="#fff" stroke-width="1.8"/></svg>
    <h3 class="spec__title">Virgin and Recycled Polypropylene</h3>
    <p class="spec__text">We can use 100% virgin polypropylene to produce your sheets. Another option is to let us recycle up to 20% of our internally regenerated polypropylene.</p>
  </div>
  <div class="spec" style="top:392px">
    <svg class="spec__icon" viewBox="0 0 40 40"><use href="#ring"/><circle cx="20" cy="20" r="7" fill="none" stroke="#fff" stroke-width="1.8"/><path d="M15 25l10-10" stroke="#fff" stroke-width="1.8"/></svg>
    <h3 class="spec__title">Custom Printing</h3>
    <p class="spec__text">Plexon sheets can be supplied with high-resolution, full-color printing. Send us your design, and we can directly print it onto the sheets in our factory.</p>
  </div>
  <div class="spec" style="top:452px">
    <svg class="spec__icon" viewBox="0 0 40 40"><use href="#ring"/><path d="M20 11c5 5 7 8 7 11a7 7 0 0 1-14 0c0-3 2-6 7-11z" fill="#fff"/><path d="M20 19c2 2 3 3 3 5a3 3 0 0 1-6 0c0-2 1-3 3-5z" fill="var(--brand)"/></svg>
    <h3 class="spec__title">Fire-Retardant Sheets</h3>
    <p class="spec__text">A fire-retardant version of Plexon sheets is available. Please let us know the fire rating you require, and we are happy to produce them for you.</p>
  </div>
  <div class="spec" style="top:512px">
    <svg class="spec__icon" viewBox="0 0 40 40"><use href="#ring"/><path d="M12 23h16M14 16v6M18 14v8M22 14v8M26 16v6" stroke="#fff" stroke-width="1.8"/></svg>
    <h3 class="spec__title">Corona Treatment</h3>
    <p class="spec__text">We give our customers the choice to print their own sheets. If you choose this option, will give the sheets a corona treatment to make sure that the sheets are well prepared for printing.</p>
  </div>
  <div class="spec" style="top:591px">
    <svg class="spec__icon" viewBox="0 0 40 40"><use href="#ring"/><path d="M20 12l7 3v5c0 4-3 7-7 8-4-1-7-4-7-8v-5z" fill="#fff"/></svg>
    <h3 class="spec__title">UV Protection</h3>
    <p class="spec__text">Plexon sheets can be produced with a UV protectant. This can extend the lifecycle of the sheets and their print work.</p>
  </div>
  <div class="spec" style="top:650px">
    <svg class="spec__icon" viewBox="0 0 40 40"><use href="#ring"/><path d="M13 27l14-14M22 13h5v5" stroke="#fff" stroke-width="2" fill="none"/></svg>
    <h3 class="spec__title">Puncture Resistance</h3>
    <p class="spec__text">We can supply our Plexon sheets in any requested puncture resistance grade. Just let us know the PR you require, and we will supply the material including a test report</p>
  </div>
</section>

<header class="band band--features">Plexon Features:</header>

<section class="features">
  <div class="feature" style="left:160px;top:808px"><svg viewBox="0 0 42 42"><use href="#disc"/><text x="21" y="27" font-size="16" font-weight="700" fill="#fff" text-anchor="middle" font-family="Cabin,sans-serif">$</text></svg>Cost Efficient</div>
  <div class="sep" style="left:212px;top:853px"></div>
  <div class="feature" style="left:271px;top:808px"><svg viewBox="0 0 42 42"><use href="#disc"/><path d="M14 27l10-10 4 4-10 10z" fill="#fff"/></svg>Easy to Install</div>
  <div class="sep" style="left:330px;top:853px"></div>
  <div class="feature" style="left:368px;top:808px"><svg viewBox="0 0 42 42"><use href="#disc"/><path d="M13 26c4-8 12-8 16-4" stroke="#fff" stroke-width="2.5" fill="none"/></svg>Strong</div>
  <div class="sep" style="left:404px;top:853px"></div>
  <div class="feature" style="left:449px;top:808px"><svg viewBox="0 0 42 42"><use href="#disc"/><path d="M15 29c2-10 7-15 13-16-1 7-6 12-13 16z" fill="#fff"/></svg>Light Weight</div>
  <div class="sep" style="left:499px;top:853px"></div>
  <div class="feature" style="left:567px;top:808px"><svg viewBox="0 0 42 42"><use href="#disc"/><path d="M12 27h18M21 13v10M17 19l4 4 4-4" stroke="#fff" stroke-width="2" fill="none"/></svg>Shock Resistant</div>
  <div class="sep" style="left:630px;top:853px"></div>
  <div class="feature" style="left:681px;top:808px"><svg viewBox="0 0 42 42"><use href="#disc"/><circle cx="21" cy="21" r="9" fill="#fff"/><path d="M21 15v6h4" stroke="var(--brand)" stroke-width="2" fill="none"/></svg>Time Saving</div>

  <div class="feature" style="left:154px;top:887px"><svg viewBox="0 0 42 42"><use href="#disc"/><path d="M11 21a10 8 0 0 1 20 0zM21 21v8a2 2 0 0 1-4 0" stroke="#fff" stroke-width="2" fill="#fff"/></svg>Waterproof</div>
  <div class="sep" style="left:203px;top:932px"></div>
  <div class="feature" style="left:254px;top:887px"><svg viewBox="0 0 42 42"><use href="#disc"/><circle cx="17" cy="17" r="3" fill="#fff"/><circle cx="25" cy="22" r="4" fill="#fff"/><circle cx="18" cy="27" r="2" fill="#fff"/></svg>Washable</div>
  <div class="sep" style="left:298px;top:932px"></div>
  <div class="feature" style="left:379px;top:887px"><svg viewBox="0 0 42 42"><use href="#disc"/><path d="M18 12h6M19 12v8l-6 10h16l-6-10v-8" stroke="#fff" stroke-width="2" fill="none"/></svg>Chemical Resistant</div>
  <div class="sep" style="left:452px;top:932px"></div>
  <div class="feature" style="left:524px;top:887px"><svg viewBox="0 0 42 42"><use href="#disc"/><rect x="13" y="15" width="16" height="13" rx="2" fill="#fff"/><path d="M21 18v7M17.5 21.5h7" stroke="var(--brand)" stroke-width="2"/></svg>Hygienic (antibacterial)</div>
  <div class="sep" style="left:600px;top:932px"></div>
  <div class="feature" style="left:680px;top:887px"><svg viewBox="0 0 42 42"><use href="#disc"/><ellipse cx="21" cy="22" rx="4" ry="6" fill="#fff"/><path d="M13 13l16 16" stroke="#fff" stroke-width="2"/></svg>Bug Resistant</div>
</section>

<header class="band band--options">K-SHIELD OPTIONS:</header>

<section class="options">
  <div class="option" style="left:94px">
    <svg class="option__icon" style="left:-63px" viewBox="0 0 40 40"><use href="#ring"/><rect x="12" y="14" width="16" height="12" fill="none" stroke="#fff" stroke-width="1.8"/><circle cx="20" cy="20" r="2.5" fill="#fff"/></svg>
    <h3 class="option__title">Specific Sizes</h3>
    <p class="option__text">We know that some projects and production lines require special sizes. That's why it is possible to order KShield products in different sizes and thicknesses.</p>
  </div>
  <div class="option" style="left:363px">
    <svg class="option__icon" style="left:-72px" viewBox="0 0 40 40"><use href="#ring"/><circle cx="20" cy="20" r="7" fill="none" stroke="#fff" stroke-width="1.8"/><path d="M15 25l10-10" stroke="#fff" stroke-width="1.8"/></svg>
    <h3 class="option__title">Logo Printing</h3>
    <p class="option__text" style="width:190px">It's possible to order K-Shield products with a custom-made print. Company logos printed on K-Shield products can be great for marketing purposes and branding.</p>
  </div>
  <div class="option" style="left:620px">
    <svg class="option__icon" style="left:-58px" viewBox="0 0 40 40"><use href="#ring"/><path d="M20 11c5 5 7 8 7 11a7 7 0 0 1-14 0c0-3 2-6 7-11z" fill="#fff"/><path d="M20 19c2 2 3 3 3 5a3 3 0 0 1-6 0c0-2 1-3 3-5z" fill="var(--brand)"/></svg>
    <h3 class="option__title">Fire-Retardant</h3>
    <p class="option__text" style="width:186px">Some K-Shield products can be produced with fire-resistant additives. K-Shield fire-rated products prevent flammability of surfaces in areas that are fire-sensitive</p>
  </div>
</section>

</body>
</html>
```